Webdesign for starlight path

"Der Sternpfad" is a new info product that will be selled through the website maybe you will create for us.

Translated from german to english the project is named "the starlight path". It´s an online video course that teaches people how to live a fulfilling, happy and healthy life.

Design paramaters
We want a serious design that embodies the real feeling of beeing happy and fulfilled. Visitors should even feel good/better when they see the website.
In color psychology some sort of calming deep green like a four-leaf clover is recommend.
Mainly the website will be the external sales page with a big video as the central attention.
We also need a member area for customers to watch our video course.

So mainly we need a eye-cathing, calming header, the content body with mainly video and just a few written words...and of course a footer for links like imprint, affiliate program etc.

What we not want:
- some kind of these exaggerated smiling photos
- that bathetic luck symbols like money or boats

Hi,

i posted a message to the design discussion. Thank you!

```html
<!DOCTYPE html>
<html lang="en">
<head>
<meta charset="utf-8">
<title>Der Sternpfad</title>
<link href="https://fonts.googleapis.com/css2?family=Marck+Script&family=Comfortaa:wght@400&display=swap" rel="stylesheet">
<style>
:root{
  --green-deep:#3f8d12;
  --green-mid:#5aa818;
  --green-light:#8cc83a;
  --green-line:#6fb32e;
  --ink:#1f3d08;
  --white:#ffffff;
  --footer-text:#808080;
  --footer-line:#dcdcdc;
  --social:#6b6b6b;
  --player:#1b1b1b;
  --poster-light:#f3f3f3;
  --poster-shade:#dedede;
}
*{margin:0;padding:0;box-sizing:border-box}
html,body{width:1200px;height:797px;overflow:hidden;background:var(--white)}
body{position:relative;font-family:Arial,Helvetica,sans-serif}
.hero{position:absolute;left:0;top:0;width:1200px;height:665px;
  background:radial-gradient(ellipse 520px 240px at 600px 90px,var(--green-light),transparent 70%),
  linear-gradient(180deg,#5fae1c 0%,var(--green-mid) 45%,var(--green-deep) 100%)}
.brand{position:absolute;left:193px;top:22px;font-family:"Marck Script",cursive;font-weight:400;font-size:41px;color:var(--white);line-height:1}
.search{position:absolute;left:701px;top:24px;width:173px;height:25px;border:2px solid #e8f3d8;
  font-size:11px;color:#d9ecc4;padding:5px 8px}
.search svg{position:absolute;right:6px;top:4px}
.login{position:absolute;left:896px;top:24px;width:122px;height:25px;border:2px solid var(--white);
  color:var(--white);font-size:13px;padding:4px 6px}
.login svg{position:absolute;right:6px;top:5px}
.rule{position:absolute;height:1px;background:var(--green-line);opacity:.8}
.nav{position:absolute;top:92px;left:0;width:1200px;font-family:"Comfortaa",sans-serif;font-size:15px;letter-spacing:-.3px;color:var(--white)}
.nav a{position:absolute;color:var(--white);text-decoration:none;white-space:nowrap;text-shadow:0 1px 1px rgba(0,0,0,.25)}
.decor{position:absolute;border-radius:50%;background:radial-gradient(circle,#49b42a 0%,rgba(60,150,20,.5) 60%,transparent 72%)}
.video{position:absolute;left:373px;top:134px;width:456px;height:276px;background:var(--player)}
.poster{position:absolute;left:0;top:0;width:456px;height:251px;
  background:linear-gradient(135deg,var(--poster-light),var(--poster-shade))}
.play{position:absolute;left:210px;top:100px}
.controls{position:absolute;left:0;top:251px;width:456px;height:25px;background:linear-gradient(#2b2b2b,#111);
  font-size:8px;color:#ddd}
.controls .time{position:absolute;left:72px;top:8px}
.btn{position:absolute;left:508px;top:435px;width:142px;height:29px;border-radius:15px;background:#151515;
  color:var(--white);font-size:13px;text-align:center;line-height:29px;box-shadow:0 2px 3px rgba(0,0,0,.4)}
.welcome{position:absolute;left:182px;top:500px;font-family:"Marck Script",cursive;font-weight:400;font-size:27px;color:var(--white);white-space:nowrap}
.intro{position:absolute;left:185px;top:543px;width:836px;font-size:10.8px;letter-spacing:-.1px;line-height:16.5px;color:var(--ink)}
.footer-clover{position:absolute;left:188px;top:615px;width:110px;height:123px;border-radius:50% 50% 45% 45%;
  background:radial-gradient(circle at 45% 40%,#7cd232,#3d9a16 70%,transparent 72%)}
.footer-line{position:absolute;left:4px;top:669px;width:1196px;height:1px;background:#b5b5b5}
.links{position:absolute;left:312px;top:688px;width:443px;font-size:11px;color:var(--footer-text)}
.links .row{height:25.7px;border-bottom:1px solid var(--footer-line);position:relative}
.links .row:last-child{border-bottom:none}
.links span{position:absolute;top:5px;white-space:nowrap}
.social{position:absolute;top:686px;width:25px;height:25px;border-radius:4px;background:var(--social)}
.copy{position:absolute;left:913px;top:723px;font-size:10px;color:#444}
</style>
</head>
<body>
<section class="hero">
  <div class="brand">Der Sternpfad</div>
  <div class="search">Enter Keyword
    <svg width="14" height="13" viewBox="0 0 14 13"><circle cx="5" cy="5" r="3.5" fill="none" stroke="#fff" stroke-width="1.6"/><line x1="7.6" y1="7.6" x2="12" y2="11.5" stroke="#fff" stroke-width="2"/></svg>
  </div>
  <div class="login">Members Login
    <svg width="14" height="12" viewBox="0 0 14 12"><polygon points="0,0 14,0 7,12" fill="#fff"/></svg>
  </div>
  <div class="rule" style="left:460px;top:59px;width:560px"></div>
  <nav class="nav">
    <a style="left:267px">Home</a>
    <a style="left:356px">About Us</a>
    <a style="left:461px">Why Choose Us</a>
    <a style="left:611px">Videos</a>
    <a style="left:700px">Blog</a>
    <a style="left:771px">Services</a>
    <a style="left:869px">Contact</a>
  </nav>
  <div class="rule" style="left:180px;top:117px;width:840px"></div>

  <div class="decor" role="img" aria-label="Clover leaves illustration" style="left:195px;top:190px;width:180px;height:180px"></div>
  <div class="decor" role="img" aria-label="Clover leaves illustration" style="left:815px;top:200px;width:210px;height:200px"></div>

  <div class="video">
    <div class="poster" role="img" aria-label="Video still: hands holding a heart"></div>
    <svg class="play" width="48" height="52" viewBox="0 0 48 52"><polygon points="0,0 48,26 0,52" fill="#2a2a2a" opacity=".85"/></svg>
    <div class="controls">
      <svg width="456" height="25" viewBox="0 0 456 25" style="position:absolute;left:0;top:0">
        <rect x="0" y="0" width="456" height="2" fill="#555"/>
        <circle cx="6" cy="1" r="3.5" fill="#ccc"/>
        <rect x="17" y="9" width="2.5" height="8" fill="#ccc"/><rect x="22" y="9" width="2.5" height="8" fill="#ccc"/>
        <polygon points="47,11 51,11 55,7 55,19 51,15 47,15" fill="#ccc"/>
        <circle cx="357" cy="13" r="4" fill="#aaa"/>
        <circle cx="379" cy="13" r="4" fill="#aaa"/>
        <rect x="397" y="10" width="10" height="6" fill="none" stroke="#ccc"/>
        <rect x="418" y="9" width="13" height="8" fill="none" stroke="#ccc"/>
        <path d="M439 9h3M439 9v3M451 9h-3M451 9v3M439 18h3M439 18v-3M451 18h-3M451 18v-3" stroke="#ccc"/>
      </svg>
      <span class="time">0:00 / 6:04</span>
    </div>
  </div>

  <div class="btn">View More Videos</div>

  <h1 class="welcome">Welcome to Der Sternpfad</h1>
  <p class="intro">Lorem ipsum dolor sit amet, consectetur adipisicing elit, sed do eiusmod tempor incididunt ut labore et dolore magna aliqua. Ut enim ad minim veniam, quis nostrud exercitation ullamco laboris nisi ut aliquip ex ea commodo consequat. Duis aute irure dolor in reprehenderit in voluptate velit esse cillum dolore eu fugiat nulla pariatur. Excepteur sint occaecat cupidatat non proident, sunt in culpa qui officia deserunt mollit anim id est laborum.</p>
  <div class="rule" style="left:180px;top:607px;width:840px"></div>
</section>

<div class="footer-line"></div>
<div class="footer-clover" role="img" aria-label="Clover illustration"></div>

<footer>
  <div class="links">
    <div class="row"><span style="left:3px">Home</span><span style="left:165px">Join Course</span><span style="left:335px">Support</span></div>
    <div class="row"><span style="left:3px">About Us</span><span style="left:165px">Services</span><span style="left:335px">FAQ</span></div>
    <div class="row"><span style="left:3px">Videos</span><span style="left:165px">Testimonials</span><span style="left:335px">Terms &amp; Conditions</span></div>
    <div class="row"><span style="left:3px">Products</span><span style="left:165px">Recent Blogs</span><span style="left:335px">Contact US</span></div>
  </div>
  <div class="social" style="left:903px"></div>
  <div class="social" style="left:939px"></div>
  <div class="social" style="left:975px"></div>
  <div class="copy">Copyright Statement</div>
</footer>
</body>
</html>
```